Business Card Design for Cybersecurity Company - Quorvent Systems

We need a business card design for our new cybersecurity company, Quorvent. We’re going for a clean, hi tech look that feels modern, premium, and trustworthy. We want a design that really stands out and makes people say WOW when we hand it over!

Quorvent delivers reliable IT support and managed services for small and mid sized businesses. We help companies stay secure, efficient, and connected through proactive monitoring, cybersecurity services, cloud management, and remote support.

Target Market(s)

Designers should target small and mid sized businesses that need dependable cybersecurity and IT support.

Industry/Entity Type

Cybersecurity, Managed Service Provider, IT services

Contact Information for Business Card

Contact information

Requirements
Must have
• The card should look clean, modern, and tech focused, with the Quorvent logo, clear contact info, and strong readability. It needs to feel premium and professional while still keeping a simple layout that fits a cybersecurity and IT brand.
Nice to have
• Nice to have elements include subtle touches that give the card a modern, tech feel, along with a layout that works well in different background styles.
Should not have
• The card should avoid clutter, loud graphics, or anything that takes attention away from the logo and contact details.

```html
<!DOCTYPE html>
<html lang="en">
<head>
<meta charset="utf-8">
<title>Quorvent Systems – Business Card</title>
<link rel="stylesheet" href="https://fonts.googleapis.com/css2?family=Montserrat:wght@400;500;600;700&display=swap">
<style>
  :root {
    --canvas: #e6e6e6;
    --card-white: #ffffff;
    --card-black: #151515;
    --ink: #2b2b2b;
    --ink-soft: #4a4a4a;
    --violet: #7b2fe0;
    --blue: #2f7bf0;
    --white: #ffffff;
  }
  * { box-sizing: border-box; margin: 0; padding: 0; }
  html, body { width: 1200px; height: 1200px; overflow: hidden; }
  body {
    background: var(--canvas);
    font-family: "Montserrat", sans-serif;
    color: var(--ink);
    display: flex;
    flex-direction: column;
    align-items: center;
    justify-content: center;
    gap: 60px;
  }
  .card {
    position: relative;
    width: 840px;
    height: 480px;
    border-radius: 28px;
    overflow: hidden;
    box-shadow: 0 14px 36px rgba(0,0,0,0.18);
  }
  .card--front { background: var(--card-white); }
  .card--back { background: linear-gradient(160deg, #222 0%, var(--card-black) 70%); }

  .wordmark { font-weight: 600; line-height: 1; }
  .wordmark__name { display: block; letter-spacing: 0.5px; }
  .wordmark__tag { display: block; font-weight: 600; letter-spacing: 11px; }

  .card--front .wordmark { position: absolute; left: 62px; top: 56px; color: var(--ink); }
  .card--front .wordmark__name { font-size: 46px; }
  .card--front .wordmark__tag { font-size: 15px; margin-top: 6px; }

  .holder { position: absolute; left: 62px; top: 168px; }
  .holder__name { font-size: 24px; font-weight: 700; letter-spacing: 0.5px; }
  .holder__title { font-size: 16px; font-weight: 400; color: var(--ink-soft); margin-top: 2px; }

  .contacts {
    position: absolute; left: 40px; right: 120px; bottom: 56px;
    display: grid;
    grid-template-columns: auto auto auto;
    column-gap: 28px; row-gap: 14px;
    font-size: 15px; font-weight: 500;
    align-items: center;
  }
  .contact { display: flex; align-items: center; gap: 10px; white-space: nowrap; }
  .contact__icon {
    width: 22px; height: 22px; border-radius: 50%;
    background: var(--violet);
    display: inline-flex; align-items: center; justify-content: center;
    flex: none;
  }
  .contact__icon svg { width: 13px; height: 13px; }
  .rule {
    position: absolute; height: 4px; border-radius: 2px;
    background: linear-gradient(90deg, var(--violet), var(--blue));
  }
  .rule--left { left: 40px; width: 310px; bottom: 34px; }
  .rule--right { left: 380px; width: 360px; bottom: 34px; }

  .circuit-art { position: absolute; }
  .card--front .circuit-art {
    right: 0; top: 170px; width: 110px; height: 220px;
    background: linear-gradient(180deg, var(--blue), var(--violet));
    clip-path: polygon(40% 0, 100% 0, 100% 100%, 40% 100%, 0 80%, 0 20%);
    opacity: 0.85;
  }
  .card--back .circuit-art {
    left: 0; top: 80px; width: 170px; height: 320px;
    background: linear-gradient(200deg, var(--blue), var(--violet));
    clip-path: polygon(0 0, 60% 0, 100% 25%, 100% 75%, 60% 100%, 0 100%);
    opacity: 0.9;
  }
  .card--back .wordmark {
    position: absolute; left: 270px; top: 170px; color: var(--white);
  }
  .card--back .wordmark__name { font-size: 72px; }
  .card--back .wordmark__tag { font-size: 20px; margin-top: 10px; letter-spacing: 16px; }
</style>
</head>
<body>
  <section class="card card--front" aria-label="Card front">
    <div class="wordmark">
      <span class="wordmark__name">Quorvent</span>
      <span class="wordmark__tag">Systems</span>
    </div>
    <div class="holder">
      <p class="holder__name">DANA MERROW</p>
      <p class="holder__title">Owner / CEO</p>
    </div>
    <div class="contacts">
      <div class="contact">
        <span class="contact__icon"><svg viewBox="0 0 24 24"><path fill="#fff" d="M6.6 10.8a15 15 0 0 0 6.6 6.6l2.2-2.2a1 1 0 0 1 1-.25 11.4 11.4 0 0 0 3.6.57 1 1 0 0 1 1 1V20a1 1 0 0 1-1 1A17 17 0 0 1 3 4a1 1 0 0 1 1-1h3.5a1 1 0 0 1 1 1c0 1.25.2 2.45.57 3.57a1 1 0 0 1-.25 1z"/></svg></span>
        Office: (855) 555-0142
      </div>
      <div class="contact">Mobile: (813) 555-0178</div>
      <div></div>
      <div class="contact">
        <span class="contact__icon"><svg viewBox="0 0 24 24"><path fill="#fff" d="M12 2a7 7 0 0 0-7 7c0 5 7 13 7 13s7-8 7-13a7 7 0 0 0-7-7zm0 9.5A2.5 2.5 0 1 1 12 6.5a2.5 2.5 0 0 1 0 5z"/></svg></span>
        Coral Point, FL
      </div>
      <div class="contact">
        <span class="contact__icon"><svg viewBox="0 0 24 24"><path fill="none" stroke="#fff" stroke-width="2.4" d="M3 6h18v12H3z M3 6l9 7 9-7"/></svg></span>
        dana@quorvent.com
      </div>
      <div class="contact">
        <span class="contact__icon"><svg viewBox="0 0 24 24"><g fill="none" stroke="#fff" stroke-width="2"><circle cx="12" cy="12" r="9"/><path d="M3 12h18M12 3c3 3 3 15 0 18M12 3c-3 3-3 15 0 18"/></g></svg></span>
        www.quorvent.com
      </div>
    </div>
    <div class="rule rule--left"></div>
    <div class="rule rule--right"></div>
    <div class="circuit-art" role="img" aria-label="Violet-to-blue circuit trace decoration"></div>
  </section>

  <section class="card card--back" aria-label="Card back">
    <div class="circuit-art" role="img" aria-label="Violet-to-blue circuit trace decoration"></div>
    <div class="wordmark">
      <span class="wordmark__name">Quorvent</span>
      <span class="wordmark__tag">Systems</span>
    </div>
  </section>
</body>
</html>
```